" Patchwork criativo e artesanato urbano O Oficina Ventarola é um local onde é oferecido cursos e aulas de bonecas, patchwork e costura criativa. Showroom de produtos para lojistas e pronta entrega de varejo. Local fomentador e propagador de arte e artesanato urbano, administrado por Lívia Damasco, artista plástica formada em Belas Artes pela IPEM. "

```html
<!DOCTYPE html>
<html lang="pt-BR">
<head>
<meta charset="utf-8">
<title>Lívia Damasco — Oficina Ventarola</title>
<link href="https://fonts.googleapis.com/css2?family=Oswald:wght@400;500;600&family=Open+Sans:wght@400;600;700&display=swap" rel="stylesheet">
<style>
:root{
  --ink:#231f20;
  --pink:#e8285a;
  --red:#e84a5f;
  --yellow:#f8c531;
  --green:#79c257;
  --teal:#3aa7c9;
  --grey:#8b8b8b;
  --light:#f3f3f3;
  --line:#dcdcdc;
  --social1:#3b5998;
  --social2:#1da1f2;
  --social3:#00aff0;
  --social4:#e2364c;
}
*{box-sizing:border-box;margin:0;padding:0}
html,body{width:1200px;height:1200px;overflow:hidden;background:#fff}
body{font-family:"Open Sans",sans-serif;color:var(--ink)}
.page{position:absolute;left:283px;top:0;width:634px;height:1200px;background:#fff}
.topline{position:absolute;left:0;top:0;width:634px;height:5px;background:var(--red)}
.brand{position:absolute;left:24px;top:22px;color:var(--ink)}
.brand-name{font-family:"Oswald",sans-serif;font-weight:600;font-size:42px;line-height:46px;letter-spacing:.5px}
.brand-tag{font-family:"Oswald",sans-serif;font-weight:600;font-size:15px;letter-spacing:2px;margin-left:60px}
.social{position:absolute;top:12px;display:flex;gap:5px}
.social span{width:17px;height:17px;border-radius:3px;display:block}
.search{position:absolute;left:360px;top:58px;display:flex}
.search-field{width:100px;height:32px;border:1px solid var(--line);border-right:0}
.search-btn{width:34px;height:32px;background:var(--ink);display:flex;align-items:center;justify-content:center}
.cart{position:absolute;left:538px;top:60px}
.cart-count{position:absolute;left:574px;top:56px;width:36px;height:36px;background:var(--red);color:#fff;font-family:"Oswald",sans-serif;font-size:16px;display:flex;align-items:center;justify-content:center}
.nav{position:absolute;left:24px;top:120px;width:586px;height:30px;background:var(--ink);display:flex;align-items:center}
.nav-welcome{font-family:"Oswald",sans-serif;color:var(--pink);font-size:14px;padding-left:12px;flex:1}
.nav a{font-family:"Oswald",sans-serif;color:#fff;font-size:13px;text-decoration:none;padding:0 8px;height:30px;line-height:30px}
.nav a.active{background:var(--red)}
.nav-plus{width:30px;height:30px;display:flex;align-items:center;justify-content:center;border-left:2px solid #fff}
.hero{position:absolute;left:24px;top:163px;width:586px;height:192px;background:linear-gradient(90deg,#c24a6a 0%,#e9b6c3 35%,#f3e4e6 55%,#b8374f 80%,#d98aa0 100%)}
.promos{position:absolute;left:24px;top:372px;width:586px;display:flex;justify-content:space-between}
.promo{width:179px;height:89px;display:flex;flex-direction:column;align-items:center;padding-top:10px}
.promo h2{font-family:"Oswald",sans-serif;font-weight:500;color:#fff;font-size:21px;line-height:24px}
.promo p{font-family:"Oswald",sans-serif;font-size:9px;color:var(--ink);margin-top:2px}
.promo .tag{margin-top:7px;font-family:"Oswald",sans-serif;font-size:17px;color:#fff;padding:0 10px;height:26px;line-height:26px}
.promo.yellow{background:var(--yellow)} .promo.yellow .tag{background:var(--red)}
.promo.red{background:var(--red)} .promo.red .tag{background:var(--teal)}
.promo.green{background:var(--green)} .promo.green .tag{background:var(--yellow)}
.section-head{position:absolute;left:24px;top:476px;width:586px;height:22px;border-bottom:1px solid var(--line);display:flex;justify-content:space-between;align-items:flex-start}
.section-head h3{font-family:"Oswald",sans-serif;font-weight:500;font-size:14px;line-height:16px}
.dept{width:190px;height:15px;background:#b7b7b7;color:#fff;font-size:8px;font-weight:600;padding-left:8px;line-height:15px;position:relative}
.dept::after{content:"";position:absolute;right:6px;top:5px;border:5px solid transparent;border-top-color:#fff}
.grid{position:absolute;left:24px;top:516px;width:586px;display:grid;grid-template-columns:repeat(4,130px);column-gap:22px;row-gap:18px}
.product{display:flex;flex-direction:column;align-items:center}
.product .photo{width:130px;height:145px;border:1px solid var(--line)}
.row2 .photo{height:160px}
.price{margin-top:14px;font-family:"Oswald",sans-serif;font-size:12px;color:#fff;padding:0 8px;height:20px;line-height:20px}
.name{margin-top:8px;font-size:7px;font-weight:700;color:var(--teal);letter-spacing:.3px;white-space:nowrap}
.actions{margin-top:8px;display:flex;gap:12px}
.p-green{background:var(--green)} .p-yellow{background:var(--yellow)} .p-red{background:var(--red)}
.footer{position:absolute;left:0;top:1027px;width:634px;height:149px;background:var(--light);display:flex;padding:12px 0 0 24px}
.footer ul{list-style:none;width:150px}
.footer li{font-size:8px;color:var(--grey);line-height:14.5px;display:flex;align-items:center;gap:7px}
.footer li::before{content:"";width:5px;height:5px;border-radius:50%;background:var(--bullet)}
.col-a{--bullet:var(--red)} .col-b{--bullet:var(--green)} .col-c{--bullet:var(--yellow)}
.footer-brand{margin-left:4px;margin-top:10px;color:var(--ink)}
.footer-brand .brand-name{font-size:25px;line-height:28px}
.footer-brand .brand-tag{font-size:10px;margin-left:34px;letter-spacing:1.5px}
.copyright{position:absolute;left:24px;top:1182px;font-size:8px;color:var(--grey)}
</style>
</head>
<body>
<div class="page">
  <div class="topline"></div>

  <header>
    <div class="brand">
      <div class="brand-name">lívia damasco</div>
      <div class="brand-tag">OFICINA VENTAROLA</div>
    </div>
    <div class="social" style="left:520px">
      <span style="background:var(--social1)"></span><span style="background:var(--social2)"></span><span style="background:var(--social3)"></span><span style="background:var(--social4)"></span>
    </div>
    <div class="search">
      <div class="search-field"></div>
      <div class="search-btn">
        <svg width="14" height="14" viewBox="0 0 14 14"><circle cx="6" cy="6" r="4.2" fill="none" stroke="#fff" stroke-width="2"/><line x1="9" y1="9" x2="13" y2="13" stroke="#fff" stroke-width="2.2"/></svg>
      </div>
    </div>
    <svg class="cart" width="26" height="24" viewBox="0 0 26 24"><path d="M1 2h4l3 13h13l3-9H7" fill="none" stroke="#231f20" stroke-width="3" stroke-linejoin="round"/><rect x="7" y="6" width="15" height="8" fill="#231f20"/><circle cx="10" cy="20" r="2.5" fill="#231f20"/><circle cx="19" cy="20" r="2.5" fill="#231f20"/></svg>
    <div class="cart-count">0</div>
  </header>

  <nav class="nav">
    <span class="nav-welcome">BEM VINDOS</span>
    <a class="active">HOME</a><a>ESTÚDIO</a><a>CADASTRO</a><a>LOGIN</a>
    <span class="nav-plus"><svg width="14" height="14" viewBox="0 0 14 14"><path d="M7 1v12M1 7h12" stroke="#fff" stroke-width="3"/></svg></span>
  </nav>

  <div class="hero" role="img" aria-label="Quarto decorado com colcha e almofadas de patchwork em tons de rosa e vermelho"></div>

  <section class="promos">
    <div class="promo yellow"><h2>LOREM IPSUM</h2><p>CLIQUE AQUI E GANHE 20% DE DESCONTO</p><span class="tag">R$ 20,00</span></div>
    <div class="promo red"><h2>LOREM IPSUM</h2><p>CLIQUE AQUI E GANHE 20% DE DESCONTO</p><span class="tag">R$ 20,00</span></div>
    <div class="promo green"><h2>LOREM IPSUM</h2><p>CLIQUE AQUI E GANHE 20% DE DESCONTO</p><span class="tag">R$ 20,00</span></div>
  </section>

  <div class="section-head">
    <h3>LANÇAMENTOS</h3>
    <div class="dept">ESCOLHA UM DEPARTAMENTO</div>
  </div>

  <section class="grid">
    <div class="product"><div class="photo" role="img" aria-label="Poltrona revestida em patchwork colorido" style="background:linear-gradient(160deg,#e9e3e0,#c9506a 60%,#7aa36a)"></div><span class="price p-green">R$129,90</span><span class="name">PUFF FLOR - ROSA &amp; VERDE</span><span class="actions"><svg width="16" height="14"><path d="M1 2h3l2 8h8l2-6H5" fill="none" stroke="#bbb" stroke-width="2"/><circle cx="7" cy="12.5" r="1.5" fill="#bbb"/><circle cx="13" cy="12.5" r="1.5" fill="#bbb"/></svg><svg width="14" height="14"><circle cx="7" cy="7" r="6.5" fill="#bbb"/><rect x="6" y="6" width="2" height="5" fill="#fff"/><rect x="6" y="3" width="2" height="2" fill="#fff"/></svg></span></div>
    <div class="product"><div class="photo" role="img" aria-label="Caixa forrada com tecido floral rosa" style="background:linear-gradient(170deg,#f1ecec,#e36f96 55%,#f2c6d6)"></div><span class="price p-yellow">R$639,00</span><span class="name">CAIXA TECIDO - FLORAL ROSA</span><span class="actions"><svg width="16" height="14"><path d="M1 2h3l2 8h8l2-6H5" fill="none" stroke="#bbb" stroke-width="2"/><circle cx="7" cy="12.5" r="1.5" fill="#bbb"/><circle cx="13" cy="12.5" r="1.5" fill="#bbb"/></svg><svg width="14" height="14"><circle cx="7" cy="7" r="6.5" fill="#bbb"/><rect x="6" y="6" width="2" height="5" fill="#fff"/><rect x="6" y="3" width="2" height="2" fill="#fff"/></svg></span></div>
    <div class="product"><div class="photo" role="img" aria-label="Puff redondo em gomos de tecidos estampados" style="background:linear-gradient(180deg,#eeeaea,#6f8fb8 45%,#c9405e 75%,#e9e3e3)"></div><span class="price p-red">R$429,00</span><span class="name">PUFF GOMOS - AZUL &amp; ROSA</span><span class="actions"><svg width="16" height="14"><path d="M1 2h3l2 8h8l2-6H5" fill="none" stroke="#bbb" stroke-width="2"/><circle cx="7" cy="12.5" r="1.5" fill="#bbb"/><circle cx="13" cy="12.5" r="1.5" fill="#bbb"/></svg><svg width="14" height="14"><circle cx="7" cy="7" r="6.5" fill="#bbb"/><rect x="6" y="6" width="2" height="5" fill="#fff"/><rect x="6" y="3" width="2" height="2" fill="#fff"/></svg></span></div>
    <div class="product"><div class="photo" role="img" aria-label="Kit de almofadas e mantas de patchwork em tons claros" style="background:linear-gradient(150deg,#f4eef0,#d8a9c6 50%,#a9c9e3)"></div><span class="price p-green">R$ 59,90</span><span class="name">KIT ALMOFADAS - TONS CLAROS</span><span class="actions"><svg width="16" height="14"><path d="M1 2h3l2 8h8l2-6H5" fill="none" stroke="#bbb" stroke-width="2"/><circle cx="7" cy="12.5" r="1.5" fill="#bbb"/><circle cx="13" cy="12.5" r="1.5" fill="#bbb"/></svg><svg width="14" height="14"><circle cx="7" cy="7" r="6.5" fill="#bbb"/><rect x="6" y="6" width="2" height="5" fill="#fff"/><rect x="6" y="3" width="2" height="2" fill="#fff"/></svg></span></div>

    <div class="product row2"><div class="photo" role="img" aria-label="Cadeira estofada com tecido estampado" style="background:linear-gradient(170deg,#f2eded,#d45674 55%,#efe6e6)"></div><span class="price p-red">R$429,00</span><span class="name">CADEIRA - FLOR VERMELHA</span><span class="actions"><svg width="16" height="14"><path d="M1 2h3l2 8h8l2-6H5" fill="none" stroke="#bbb" stroke-width="2"/><circle cx="7" cy="12.5" r="1.5" fill="#bbb"/><circle cx="13" cy="12.5" r="1.5" fill="#bbb"/></svg><svg width="14" height="14"><circle cx="7" cy="7" r="6.5" fill="#bbb"/><rect x="6" y="6" width="2" height="5" fill="#fff"/><rect x="6" y="3" width="2" height="2" fill="#fff"/></svg></span></div>
    <div class="product row2"><div class="photo" role="img" aria-label="Conjunto de louça com estampa floral" style="background:linear-gradient(170deg,#d7dcc6,#f0e6de 45%,#c98aa0)"></div><span class="price p-yellow">R$429,00</span><span class="name">JOGO DE CHÁ - FLORAL</span><span class="actions"><svg width="16" height="14"><path d="M1 2h3l2 8h8l2-6H5" fill="none" stroke="#bbb" stroke-width="2"/><circle cx="7" cy="12.5" r="1.5" fill="#bbb"/><circle cx="13" cy="12.5" r="1.5" fill="#bbb"/></svg><svg width="14" height="14"><circle cx="7" cy="7" r="6.5" fill="#bbb"/><rect x="6" y="6" width="2" height="5" fill="#fff"/><rect x="6" y="3" width="2" height="2" fill="#fff"/></svg></span></div>
    <div class="product row2"><div class="photo" role="img" aria-label="Baú decorado em tons de vinho e lilás" style="background:linear-gradient(170deg,#efeaea,#7b4a63 50%,#c7a9be)"></div><span class="price p-red">R$533,15</span><span class="name">BAÚ LILÁS - VINHO</span><span class="actions"><svg width="16" height="14"><path d="M1 2h3l2 8h8l2-6H5" fill="none" stroke="#bbb" stroke-width="2"/><circle cx="7" cy="12.5" r="1.5" fill="#bbb"/><circle cx="13" cy="12.5" r="1.5" fill="#bbb"/></svg><svg width="14" height="14"><circle cx="7" cy="7" r="6.5" fill="#bbb"/><rect x="6" y="6" width="2" height="5" fill="#fff"/><rect x="6" y="3" width="2" height="2" fill="#fff"/></svg></span></div>
    <div class="product row2"><div class="photo" role="img" aria-label="Bicho de pano em tecido estampado" style="background:linear-gradient(170deg,#f2eeee,#d2c3cf 45%,#b8485f)"></div><span class="price p-yellow">R$648,25</span><span class="name">BICHO DE PANO - ROSA</span><span class="actions"><svg width="16" height="14"><path d="M1 2h3l2 8h8l2-6H5" fill="none" stroke="#bbb" stroke-width="2"/><circle cx="7" cy="12.5" r="1.5" fill="#bbb"/><circle cx="13" cy="12.5" r="1.5" fill="#bbb"/></svg><svg width="14" height="14"><circle cx="7" cy="7" r="6.5" fill="#bbb"/><rect x="6" y="6" width="2" height="5" fill="#fff"/><rect x="6" y="3" width="2" height="2" fill="#fff"/></svg></span></div>
  </section>

  <footer class="footer">
    <ul class="col-a"><li>PRODUTOS NATAL</li><li>PINTURA</li><li>TECIDOS</li><li>DESENHOS</li><li>MOLDES</li><li>SOLEÇÕES</li></ul>
    <ul class="col-b"><li>Ofertas Especiais</li><li>Novos Produtos</li><li>Mais Vendidos</li><li>Outros Produtos</li><li>Contate-nos</li><li>Mapa do Site</li></ul>
    <ul class="col-c"><li>Minhas Compras</li><li>Minha conta</li><li>Meus Dados</li><li>Meu endereço</li><li>Meus produtos favoritos</li></ul>
    <div class="footer-brand">
      <div class="brand-name">lívia damasco</div>
      <div class="brand-tag">OFICINA VENTAROLA</div>
    </div>
  </footer>
  <div class="social" style="left:526px;top:1110px">
    <span style="background:var(--social1)"></span><span style="background:var(--social2)"></span><span style="background:var(--social3)"></span><span style="background:var(--social4)"></span>
  </div>
  <div class="copyright">© 2013 Powered by AGULHA DIGITAL</div>
</div>
</body>
</html>
```